Need website redesign!

I have a site, www.pinehavenfitcamp.example

I am looking to have it redesigned to make it simpler, and encourage people who hit the home page to click on a service, opt in, or contact me for more info. Having a video front and center with icons representing the services we offer around it may be a good idea, but I am open to YOUR design. Conversion is my goal. I want it to be friendly, but convey the fun and ENERGY of my bootcamp. Scrolling pics on home page so people can get a feel for our bootcamp is recommended as well.

```html
<!DOCTYPE html>
<html lang="en">
<head>
<meta charset="utf-8">
<title>Pinehaven Fit Camp</title>
<link href="https://fonts.googleapis.com/css2?family=Oswald:wght@300;400;500&family=Open+Sans:wght@400&display=swap" rel="stylesheet">
<style>
  :root{
    --page:#1f1f1f;
    --topbar:#252525;
    --panel:#0d0d0d;
    --card:#1c1c1c;
    --red:#d8232a;
    --red-dark:#b51a20;
    --white:#ffffff;
    --text:#cfcfcf;
    --muted:#8a8a8a;
    --icon:#9a9a9a;
  }
  *{margin:0;padding:0;box-sizing:border-box}
  html,body{width:763px;height:1200px;overflow:hidden}
  body{position:relative;background:linear-gradient(90deg,#2e2e2e 0%,#1d1d1d 8%,#1d1d1d 92%,#2e2e2e 100%);font-family:"Open Sans",Arial,sans-serif;color:var(--text)}
  .abs{position:absolute}
  .head-font{font-family:"Oswald","Arial Narrow",sans-serif;font-weight:300}
  .topbar{left:0;top:0;width:763px;height:78px;background:var(--topbar)}
  .navbar{left:0;top:78px;width:763px;height:36px;background:linear-gradient(#e32b31,var(--red-dark))}
  .nav-link{top:78px;height:36px;line-height:36px;font-family:"Oswald","Arial Narrow",sans-serif;font-weight:400;font-size:10.5px;color:var(--white)}
  .nav-sep{top:82px;width:1px;height:28px;background:rgba(0,0,0,.18)}
  .content-panel{left:63px;top:114px;width:638px;height:1018px;background:var(--panel)}
  .brand-badge{left:318px;top:30px;width:142px;height:136px;border-radius:50%;background:#161616;display:flex;flex-direction:column;align-items:center;justify-content:center;text-align:center;box-shadow:0 0 0 2px #111}
  .brand-name{font-family:"Oswald","Arial Narrow",sans-serif;font-weight:500;font-size:19px;line-height:22px;color:var(--red);text-transform:uppercase}
  .site{font-size:6px;color:var(--white);margin-top:6px;letter-spacing:.1px}
  .hero{left:81px;top:138px;width:603px;height:320px;border-radius:3px;overflow:hidden;
    background:
      radial-gradient(ellipse 70px 60px at 175px 72px,rgba(190,150,125,.55),transparent 70%),
      radial-gradient(ellipse 110px 55px at 150px 140px,rgba(200,60,40,.55),transparent 70%),
      radial-gradient(ellipse 120px 60px at 175px 245px,rgba(170,125,100,.55),transparent 70%),
      radial-gradient(ellipse 140px 70px at 330px 150px,rgba(120,105,95,.5),transparent 70%),
      linear-gradient(180deg,rgba(0,0,0,0) 70%,rgba(20,20,20,.7) 100%),
      linear-gradient(100deg,#8a8a8a 0%,#6a6a6a 30%,#484848 60%,#3a3a3a 100%)}
  .hero-brand{left:496px;top:205px;width:124px;text-align:center}
  .hero-brand .brand-name{font-size:17px;line-height:20px}
  .hero-title{left:455px;top:296px;width:206px;text-align:center;font-family:"Oswald","Arial Narrow",sans-serif;font-weight:500;font-size:18.5px;line-height:30px;color:var(--white)}
  .slider-arrow{top:367px;width:22px;height:22px;border-radius:50%;background:#1c1c1c;border:1px solid #555}
  .intro-photo{left:81px;top:483px;width:157px;height:159px;background:linear-gradient(135deg,#e2e6e8,#c9b29a 55%,#8c8f93)}
  .intro-title{left:254px;top:481px;font-size:12px;color:var(--white);font-weight:300}
  .intro-text{left:254px;top:511px;width:210px;font-size:7.6px;line-height:14px;color:var(--muted)}
  .intro-text p+p{margin-top:8px}
  .btn-outline{left:254px;top:618px;width:57px;height:24px;border:1px solid #333;border-radius:2px;font-size:7.5px;line-height:22px;text-align:center;color:var(--muted)}
  .video{left:490px;top:481px;width:193px;height:157px;background:#2a2a2a;border:1px solid #3a3a3a;padding:4px}
  .video-fill{width:100%;height:100%;background:linear-gradient(160deg,#8fa2a8,#c9b089 50%,#9a7a58)}
  .newsletter{left:80px;top:662px;width:603px;height:56px;background:var(--card);border-radius:2px}
  .news-title{left:94px;top:670px;font-size:14.5px;color:var(--white)}
  .news-title span{color:var(--red)}
  .news-sub{left:94px;top:695px;font-size:7.5px;color:var(--muted)}
  .field{top:679px;width:109px;height:23px;background:#262626;border:1px solid #2f2f2f;border-radius:2px;font-size:6.5px;line-height:21px;padding-left:8px;color:#666}
  .btn-red{left:587px;top:679px;width:85px;height:23px;background:var(--red);border-radius:2px;font-family:"Oswald","Arial Narrow",sans-serif;font-weight:400;font-size:9.5px;line-height:23px;text-align:center;color:var(--white)}
  .section-title{font-size:12px;color:var(--white);font-weight:300}
  .location-box{left:79px;top:774px;width:135px;height:110px;background:var(--card);border-radius:2px;padding:12px;font-size:7.4px;line-height:13px;color:var(--muted)}
  .location-box p+p{margin-top:8px;padding-left:3px}
  .service-list{left:80px;top:929px;list-style:none}
  .service-list li{height:21.8px;font-size:8.5px;color:var(--muted);display:flex;align-items:center}
  .service-list svg{margin-right:9px}
  .class-item{left:248px;width:437px;height:94px}
  .class-photo{position:absolute;left:0;top:0;width:143px;height:94px;border:1px solid #444}
  .class-title{position:absolute;left:158px;top:0;font-family:"Oswald","Arial Narrow",sans-serif;font-weight:300;font-size:10.5px;color:var(--white)}
  .class-text{position:absolute;left:158px;top:21px;width:280px;font-size:6.8px;line-height:13px;color:#6a6a6a}
  .class-more{position:absolute;left:158px;top:82px;font-size:8px;color:var(--muted);text-decoration:underline}
  .footer-links{left:78px;top:1150px;font-size:7.2px;color:#aaa}
  .copyright{left:78px;top:1170px;font-size:7.5px;color:#aaa}
  .copyright span{color:var(--red)}
  .social{top:1157px;width:18px;height:18px;border-radius:50%;border:1px solid #777;display:flex;align-items:center;justify-content:center}
</style>
</head>
<body>
  <div class="abs topbar"></div>
  <div class="abs navbar"></div>

  <a class="abs nav-link" style="left:79px">HOME</a>
  <span class="abs nav-sep" style="left:114px"></span>
  <a class="abs nav-link" style="left:134px">ABOUT US</a>
  <span class="abs nav-sep" style="left:186px"></span>
  <a class="abs nav-link" style="left:203px">SERVICES</a>
  <span class="abs nav-sep" style="left:253px"></span>
  <a class="abs nav-link" style="left:270px">FAQ'S</a>
  <a class="abs nav-link" style="left:485px">CLASSES</a>
  <span class="abs nav-sep" style="left:534px"></span>
  <a class="abs nav-link" style="left:550px">BOOTCAMPS</a>
  <span class="abs nav-sep" style="left:612px"></span>
  <a class="abs nav-link" style="left:628px">CONTACT US</a>

  <div class="abs content-panel"></div>

  <div class="abs brand-badge"><div class="brand-name">Pinehaven<br>Fit Camp</div><div class="site">PINEHAVENFITCAMP.EXAMPLE</div></div>

  <div class="abs hero" role="img" aria-label="Photo of a man and a woman holding a plank on a gym floor"></div>
  <div class="abs hero-brand"><div class="brand-name">Pinehaven<br>Fit Camp</div><div class="site">PINEHAVENFITCAMP.EXAMPLE</div></div>
  <div class="abs hero-title">PROGRAMS MEMBERS<br>ONLY WORKOUTS &amp; MORE!</div>
  <svg class="abs slider-arrow" style="left:531px" viewBox="0 0 22 22"><path d="M13 6 L8 11 L13 16" fill="none" stroke="#fff" stroke-width="1.6"/></svg>
  <svg class="abs slider-arrow" style="left:559px" viewBox="0 0 22 22"><path d="M9 6 L14 11 L9 16" fill="none" stroke="#fff" stroke-width="1.6"/></svg>

  <div class="abs intro-photo" role="img" aria-label="Photo of a smiling group doing sit-ups in a fitness class"></div>
  <h2 class="abs intro-title head-font">WHAT IS PINEHAVEN FIT CAMP?</h2>
  <div class="abs intro-text">
    <p>Lorem ipsum dolor sit amet, consectetur adipiscing elit, sed do eiusmod tempor incididunt ut labore et dolore magna aliqua. Ut enim ad minim veniam, quis nostrud exercitation ullamco laboris nisi ut</p>
    <p>Duis aute irure dolor in reprehenderit in voluptate velit cillum dolore eu fugiat nulla pariatur....</p>
  </div>
  <a class="abs btn-outline">READ MORE</a>

  <div class="abs video"><div class="video-fill" role="img" aria-label="Video still of a group class doing crunches on mats"></div></div>
  <svg class="abs" style="left:557px;top:532px" width="52" height="52" viewBox="0 0 52 52"><circle cx="26" cy="26" r="24" fill="none" stroke="#fff" stroke-width="3.5"/><path d="M20 15 L37 26 L20 37 Z" fill="#fff"/></svg>

  <div class="abs newsletter"></div>
  <h2 class="abs news-title head-font">NEWSLETTER <span>SIGN-UP</span></h2>
  <p class="abs news-sub">Leave your email for a FREE week of bootcamp, NO OBLIGATION</p>
  <div class="abs field" style="left:344px">Name</div>
  <div class="abs field" style="left:467px">E - Mail</div>
  <a class="abs btn-red">GET STARTED NOW!</a>

  <h2 class="abs section-title head-font" style="left:79px;top:744px">OUR LOCATIONS</h2>
  <div class="abs location-box">
    <p>Ridgefield Martial Arts Studio 1180 Alder Lane Meadow Point Building Pinehaven, ST 00110</p>
    <p>402 Market Row Suite B Cedar Falls, ST 00120</p>
  </div>

  <h2 class="abs section-title head-font" style="left:79px;top:900px">OUR SERVICES</h2>
  <ul class="abs service-list">
    <li><svg width="8" height="8" viewBox="0 0 8 8"><circle cx="4" cy="4" r="4" fill="#555"/><path d="M3 2 L5 4 L3 6" fill="none" stroke="#111" stroke-width="1.2"/></svg>Boot Camp</li>
    <li><svg width="8" height="8" viewBox="0 0 8 8"><circle cx="4" cy="4" r="4" fill="#555"/><path d="M3 2 L5 4 L3 6" fill="none" stroke="#111" stroke-width="1.2"/></svg>Small Group Training</li>
    <li><svg width="8" height="8" viewBox="0 0 8 8"><circle cx="4" cy="4" r="4" fill="#555"/><path d="M3 2 L5 4 L3 6" fill="none" stroke="#111" stroke-width="1.2"/></svg>Personal Training</li>
    <li><svg width="8" height="8" viewBox="0 0 8 8"><circle cx="4" cy="4" r="4" fill="#555"/><path d="M3 2 L5 4 L3 6" fill="none" stroke="#111" stroke-width="1.2"/></svg>Specialty Training</li>
    <li><svg width="8" height="8" viewBox="0 0 8 8"><circle cx="4" cy="4" r="4" fill="#555"/><path d="M3 2 L5 4 L3 6" fill="none" stroke="#111" stroke-width="1.2"/></svg>Yoga</li>
    <li><svg width="8" height="8" viewBox="0 0 8 8"><circle cx="4" cy="4" r="4" fill="#555"/><path d="M3 2 L5 4 L3 6" fill="none" stroke="#111" stroke-width="1.2"/></svg>Kids Sports/Agility</li>
    <li><svg width="8" height="8" viewBox="0 0 8 8"><circle cx="4" cy="4" r="4" fill="#555"/><path d="M3 2 L5 4 L3 6" fill="none" stroke="#111" stroke-width="1.2"/></svg>Corporate Training</li>
  </ul>

  <h2 class="abs section-title head-font" style="left:248px;top:744px">OUR CLASSES</h2>

  <div class="abs class-item" style="top:776px">
    <div class="class-photo" role="img" aria-label="Photo of suspension strap training in a gym" style="background:linear-gradient(135deg,#d2d2d2,#6d6d6d 50%,#2c4c9a)"></div>
    <h3 class="class-title">If you're in Eastern Pine Valley</h3>
    <p class="class-text">Lorem ipsum dolor sit amet, consectetur adipiscing elit, sed do eiusmod tempor incididunt ut labore et dolore magna aliqua. Ut enim ad minim veniam, quis nostrud exercitation ullamco laboris nisi ut aliquip ex ea commodo consequat. Duis aute irure dolor in reprehenderit in voluptate velit esse cillum dolore</p>
    <a class="class-more">READ MORE</a>
  </div>

  <div class="abs class-item" style="top:891px">
    <div class="class-photo" role="img" aria-label="Photo of a group class stretching on mats" style="background:linear-gradient(135deg,#d6d6d6,#8a8a8a 50%,#c8358f)"></div>
    <h3 class="class-title">If you're in Eastern Pine Valley</h3>
    <p class="class-text">Lorem ipsum dolor sit amet, consectetur adipiscing elit, sed do eiusmod tempor incididunt ut labore et dolore magna aliqua. Ut enim ad minim veniam, quis nostrud exercitation ullamco laboris nisi ut aliquip ex ea commodo consequat. Duis aute irure dolor in reprehenderit in voluptate velit esse cillum dolore</p>
    <a class="class-more">READ MORE</a>
  </div>

  <div class="abs class-item" style="top:1006px">
    <div class="class-photo" role="img" aria-label="Photo of a group exercising outdoors on a lawn" style="background:linear-gradient(160deg,#9bc25a,#5e8a2e 55%,#d9a7b8)"></div>
    <h3 class="class-title">If you're in Eastern Pine Valley</h3>
    <p class="class-text">Lorem ipsum dolor sit amet, consectetur adipiscing elit, sed do eiusmod tempor incididunt ut labore et dolore magna aliqua. Ut enim ad minim veniam, quis nostrud exercitation ullamco laboris nisi ut aliquip ex ea commodo consequat. Duis aute irure dolor in reprehenderit in voluptate velit esse cillum dolore</p>
    <a class="class-more">READ MORE</a>
  </div>

  <nav class="abs footer-links">Home / &nbsp;About Us &nbsp;/ &nbsp;Services &nbsp;/ &nbsp;Classes &nbsp;/ &nbsp;FAQ's &nbsp;/ &nbsp;Bootcamps</nav>
  <p class="abs copyright">©2013 - 2014 &nbsp;<span>Pinehaven Fit Camp</span> . All Rights Reserved.</p>

  <a class="abs social" style="left:580px" aria-label="Email"><svg width="10" height="10" viewBox="0 0 10 10"><rect x="1" y="2.5" width="8" height="5.5" fill="none" stroke="var(--icon)" stroke-width="1"/><path d="M1 2.5 L5 5.6 L9 2.5" fill="none" stroke="var(--icon)" stroke-width="1"/></svg></a>
  <a class="abs social" style="left:601px" aria-label="Chat"><svg width="10" height="10" viewBox="0 0 10 10"><path d="M1.5 2 H8.5 V6.5 H4.5 L2.5 8.5 V6.5 H1.5 Z" fill="none" stroke="var(--icon)" stroke-width="1"/></svg></a>
  <a class="abs social" style="left:623px" aria-label="Location"><svg width="10" height="10" viewBox="0 0 10 10"><path d="M5 9 C3 6.5 2 5 2 3.8 A3 3 0 0 1 8 3.8 C8 5 7 6.5 5 9 Z" fill="none" stroke="var(--icon)" stroke-width="1"/><circle cx="5" cy="3.8" r="1" fill="var(--icon)"/></svg></a>
  <a class="abs social" style="left:645px" aria-label="Phone"><svg width="10" height="10" viewBox="0 0 10 10"><path d="M2.5 1.5 L4 1.5 L4.8 3.5 L3.8 4.3 C4.3 5.4 4.8 5.9 5.8 6.3 L6.6 5.3 L8.5 6.1 L8.5 7.6 C8.5 8.2 8 8.6 7.4 8.5 C4.4 8 2 5.6 1.5 2.6 C1.4 2 1.8 1.5 2.5 1.5 Z" fill="var(--icon)"/></svg></a>
  <a class="abs social" style="left:666px" aria-label="Video"><svg width="10" height="10" viewBox="0 0 10 10"><path d="M3.5 2.5 L7.5 5 L3.5 7.5 Z" fill="var(--icon)"/></svg></a>
</body>
</html>
```